The maple crew

I want it as prefession and attractive as possible we are a lawnmowing business

Phone number 605-318-2264
Name- Carlos Whitfield
Email- themaplecrewsd@fernpost.com

```html
<!DOCTYPE html>
<html lang="en">
<head>
<meta charset="utf-8">
<title>The Maple Crew — Business Cards</title>
<link href="https://fonts.googleapis.com/css2?family=Poppins:wght@400;600;700&display=swap" rel="stylesheet">
<style>
  :root {
    --backdrop: #eceae6;
    --card-white: #ffffff;
    --brand-dark: #1d6a36;
    --brand-back: #15663a;
    --brand-back-light: #1b7042;
    --ink: #1f5f33;
    --muted: #6f8f78;
    --on-dark: #ffffff;
  }
  * { box-sizing: border-box; margin: 0; padding: 0; }
  html, body {
    width: 1200px; height: 1200px; overflow: hidden;
    background: var(--backdrop);
    font-family: "Poppins", sans-serif;
  }
  .sheet { position: relative; width: 1200px; height: 1200px; }
  .card {
    position: absolute; top: 250px;
    width: 460px; height: 700px;
    border-radius: 4px;
    box-shadow: 0 10px 28px rgba(0,0,0,0.18);
    overflow: hidden;
  }
  .card--front { left: 125px; background: var(--card-white); }
  .card--back { left: 620px; background: var(--brand-back); }

  .wordmark {
    display: flex; align-items: center; justify-content: center; gap: 12px;
    font-weight: 700; font-size: 38px; letter-spacing: 0.5px;
    text-transform: uppercase; white-space: nowrap;
  }
  .wordmark__dot { width: 16px; height: 16px; border-radius: 50%; flex: none; }
  .card--front .wordmark { position: absolute; top: 160px; left: 0; right: 0; color: var(--brand-dark); }
  .card--front .wordmark__dot { background: var(--brand-dark); }

  .contact-name {
    position: absolute; top: 355px; left: 0; right: 0; text-align: center;
    font-weight: 700; font-size: 36px; color: var(--ink);
  }
  .contact-role {
    position: absolute; top: 412px; left: 0; right: 0; text-align: center;
    font-weight: 400; font-size: 17px; color: var(--muted); letter-spacing: 1px;
  }
  .contact-list {
    position: absolute; top: 480px; left: 0; right: 0;
    display: flex; flex-direction: column; align-items: center; gap: 16px;
    list-style: none; font-size: 20px; color: var(--ink);
  }
  .contact-list li { display: flex; align-items: center; gap: 12px; }
  .contact-list svg { width: 24px; height: 24px; fill: var(--ink); flex: none; }

  .back-pattern {
    position: absolute; inset: 0;
    background: linear-gradient(160deg, var(--brand-back-light), var(--brand-back) 60%);
  }
  .card--back .wordmark {
    position: absolute; top: 325px; left: 0; right: 0; color: var(--on-dark);
  }
  .card--back .wordmark__dot { background: var(--on-dark); }
</style>
</head>
<body>
<main class="sheet">
  <section class="card card--front">
    <div class="wordmark"><span class="wordmark__dot"></span>The Maple Crew</div>
    <h1 class="contact-name">Carlos Whitfield</h1>
    <p class="contact-role">Owner and Operator</p>
    <ul class="contact-list">
      <li>
        <svg viewBox="0 0 24 24" aria-hidden="true"><path d="M6.6 10.8a15.1 15.1 0 0 0 6.6 6.6l2.2-2.2a1 1 0 0 1 1-.25 11.4 11.4 0 0 0 3.6.57 1 1 0 0 1 1 1V20a1 1 0 0 1-1 1A17 17 0 0 1 3 4a1 1 0 0 1 1-1h3.5a1 1 0 0 1 1 1c0 1.25.2 2.45.57 3.57a1 1 0 0 1-.25 1z"/></svg>
        605-318-2264
      </li>
      <li>
        <svg viewBox="0 0 24 24" aria-hidden="true"><path d="M2 5h20v14H2zm2 2v.4l8 5.2 8-5.2V7zm0 2.8V17h16V9.8l-8 5.2z"/></svg>
        themaplecrewsd@fernpost.com
      </li>
    </ul>
  </section>

  <section class="card card--back">
    <div class="back-pattern" role="img" aria-label="Faint repeating pattern of lawn mower figures on green"></div>
    <div class="wordmark"><span class="wordmark__dot"></span>The Maple Crew</div>
  </section>
</main>
</body>
</html>
```